Sale- Bundle signs

We are looking for a design to use for Permanent SALE/Bundle deal signs. We are a natural bath products company who uses all natural ingredients to create our handmade line of natural products. We love a clean, fresh look and feel. Simple eye-catching that will be a quick glance and they will know the offer.
We would like to have something simple, eye catching that will promote sales on our different products.
Dead Sea Salt Body Scrubs
large 2 for $40
small 3 for $20
Moisturizing Wash with coconut & olive oil
2 for $20
There are several more needed but we are hoping to decide on one template before making all of the signs.
Visit our website here www.bramblecovewash.com
Target Market(s)
Our store serves 70% women and the majority of our customers are 30+ years old.
Industry/Entity Type
It Company
Font styles to use
Other font styles liked:
- Century Gothic or similar

```html
<!DOCTYPE html>
<html lang="en">
<head>
<meta charset="utf-8">
<title>Bramble Cove – Bundle Deal Signs</title>
<link rel="stylesheet" href="https://fonts.googleapis.com/css2?family=Questrial&family=Arimo:wght@700&display=swap">
<style>
  :root {
    --sky: #0b93cf;
    --teal: #34ae9a;
    --sun: #f2c230;
    --tangerine: #e8853f;
    --navy: #1f2d3a;
    --white: #ffffff;
    --olive: #5b7f2e;
    --leaf: #86c440;
    --ink: #3a3a3a;
  }
  html, body {
    margin: 0;
    padding: 0;
    width: 1200px;
    height: 833px;
    overflow: hidden;
    background: var(--white);
  }
  .sign-sheet { display: block; width: 1200px; height: 833px; }
  .brand-name { font-family: "Questrial", sans-serif; font-size: 54px; }
  .brand-tagline { font-family: "Questrial", sans-serif; font-size: 19px; letter-spacing: 0.3px; }
  .product-title { font-family: "Arimo", Arial, sans-serif; font-weight: 700; font-size: 15px; fill: var(--white); }
  .size-label { font-family: "Questrial", sans-serif; font-size: 28px; fill: var(--navy); font-weight: 700; }
  .price { font-family: "Arimo", Arial, sans-serif; font-weight: 700; font-size: 42px; fill: var(--white); }
  .wash-title { font-family: "Arimo", Arial, sans-serif; font-weight: 700; font-size: 14px; fill: var(--navy); }
  .website { font-family: "Arimo", Arial, sans-serif; font-weight: 700; font-size: 12.5px; fill: var(--navy); }
  .website-name { fill: var(--olive); }
  .bg-sky { fill: var(--sky); }
  .bg-white { fill: var(--white); stroke: var(--sun); stroke-width: 1; }
  .shape-teal { fill: var(--teal); }
  .shape-sun { fill: var(--sun); }
  .shape-tangerine { fill: var(--tangerine); }
</style>
</head>
<body>
<svg class="sign-sheet" viewBox="0 0 1000 694" xmlns="http://www.w3.org/2000/svg">

  <!-- Sign: blue edition -->
  <g class="sign sign--blue">
    <rect class="bg-sky" x="28" y="27" width="452" height="631"/>
    <polygon class="shape-sun" points="28,66 402,268 28,658"/>
    <polygon class="shape-sun" points="28,658 28,560 200,520 300,658"/>
    <polygon class="shape-teal" points="36,84 376,270 36,620"/>
    <polygon class="shape-sun" points="172,500 480,182 480,600 436,658 300,658"/>
    <polygon class="shape-tangerine" points="186,502 472,204 472,582 424,650"/>

    <text class="brand-name" x="452" y="102" text-anchor="end" fill="var(--white)">bramble cove</text>
    <text class="brand-tagline" x="452" y="130" text-anchor="end" fill="var(--white)">NATURAL BATH PRODUCTS</text>

    <text class="product-title" x="148" y="224" text-anchor="middle">DEAD SEA SALT</text>
    <text class="product-title" x="148" y="246" text-anchor="middle">BODY SCRUBS</text>
    <text class="size-label" x="145" y="286" text-anchor="middle">Large 2</text>
    <text class="price" x="145" y="336" text-anchor="middle">for $40</text>
    <text class="size-label" x="145" y="389" text-anchor="middle">Small 3</text>
    <text class="price" x="145" y="428" text-anchor="middle">for $20</text>

    <text class="wash-title" x="372" y="417" text-anchor="middle">MOISTURIZING WASH</text>
    <text class="wash-title" x="372" y="437" text-anchor="middle">WITH</text>
    <text class="wash-title" x="372" y="457" text-anchor="middle">COCONUT &amp; OLIVE OIL</text>
    <text class="price" x="366" y="532" text-anchor="middle">2 for $20</text>

    <text class="website" x="58" y="638">www.<tspan class="website-name">bramblecovewash</tspan>.com</text>
  </g>

  <!-- Sign: white edition -->
  <g class="sign sign--white" transform="translate(485,0)">
    <rect class="bg-white" x="28.5" y="27.5" width="451" height="630"/>
    <polygon class="shape-sun" points="29,66 402,268 29,657"/>
    <polygon class="shape-sun" points="29,657 29,560 200,520 300,657"/>
    <polygon class="shape-teal" points="36,84 376,270 36,620"/>
    <polygon class="shape-sun" points="172,500 479,182 479,600 436,657 300,657"/>
    <polygon class="shape-tangerine" points="186,502 472,204 472,582 424,650"/>

    <text class="brand-name" x="452" y="102" text-anchor="end" fill="var(--olive)">bramble cove</text>
    <text class="brand-tagline" x="452" y="130" text-anchor="end" fill="var(--olive)">NATURAL BATH PRODUCTS</text>

    <text class="product-title" x="148" y="224" text-anchor="middle">DEAD SEA SALT</text>
    <text class="product-title" x="148" y="246" text-anchor="middle">BODY SCRUBS</text>
    <text class="size-label" x="145" y="286" text-anchor="middle">Large 2</text>
    <text class="price" x="145" y="336" text-anchor="middle">for $40</text>
    <text class="size-label" x="145" y="389" text-anchor="middle">Small 3</text>
    <text class="price" x="145" y="428" text-anchor="middle">for $20</text>

    <text class="wash-title" x="372" y="417" text-anchor="middle">MOISTURIZING WASH</text>
    <text class="wash-title" x="372" y="437" text-anchor="middle">WITH</text>
    <text class="wash-title" x="372" y="457" text-anchor="middle">COCONUT &amp; OLIVE OIL</text>
    <text class="price" x="366" y="532" text-anchor="middle">2 for $20</text>

    <text class="website" x="58" y="638">www.<tspan class="website-name">bramblecovewash</tspan>.com</text>
  </g>
</svg>
</body>
</html>
```